Policy Manual in Education

I need the attached document to be put in a publishable format, with graphics a professional layout, and something that looks more like a professional report, etc. Use color samples from http://www.brvt-lo.com/ and www.kt7up.com, my company is Kt7up, we were hired to write the report and we also built the BRVT resource center http://www.brvt-lo.com/ .

Education

• Look and feel around NM. http://www.brvt-lo.com/ and www.kt7up.com

```html
<!DOCTYPE html>
<html lang="en">
<head>
<meta charset="utf-8">
<title>Policy Manual in Education</title>
<link href="https://fonts.googleapis.com/css2?family=Arimo:ital,wght@0,400;0,700;1,400;1,700&display=swap" rel="stylesheet">
<style>
:root{
  --desk:#9aa3ad;
  --ruler:#e4e8ee;
  --ruler-ink:#5a5f66;
  --page:#ffffff;
  --ink:#1a1a1a;
  --heading:#1f3d6b;
  --quote:#5b7fb5;
  --brand:#e9b25a;
  --rule:#c9d3de;
  --muted:#555a60;
}
*{box-sizing:border-box;margin:0;padding:0}
html,body{width:1200px;height:743px;overflow:hidden}
body{background:var(--desk);position:relative;font-family:"Arimo",Arial,sans-serif;color:var(--ink)}
.ruler{position:absolute;left:0;top:0;width:614px;height:18px;background:var(--ruler);border-bottom:1px solid #b9c0c8;
  font-size:10px;color:var(--ruler-ink);letter-spacing:8.4px;line-height:18px;padding-left:60px;white-space:nowrap;overflow:hidden}
.page{position:absolute;background:var(--page);box-shadow:0 1px 3px rgba(0,0,0,.35)}
.page--left{left:55px;top:22px;width:556px;height:697px}
.page--right{left:623px;top:22px;width:557px;height:697px}
.page--next-left{left:55px;top:728px;width:556px;height:40px}
.page--next-right{left:623px;top:728px;width:557px;height:40px}
.page-brand{position:absolute;top:-5px;left:0;right:0;text-align:center;font-size:9px;font-weight:700;color:var(--brand);line-height:12px}
.page-rule{position:absolute;top:27px;left:0;right:0;border-top:1px solid var(--rule)}
.page-body{position:absolute;left:64px;top:40px;width:429px;font-size:11.2px;line-height:14.6px}
.page--right .page-body{left:66px;top:45px;width:427px}
.page-body p{text-align:justify;margin-bottom:14.6px}
.page-body p.indent{text-indent:32px}
.section-title{color:var(--heading);font-size:16px;font-weight:700;line-height:22px;margin:20px 0 19px;padding-left:30px;text-indent:-30px}
.page--right .section-title{margin:12px 0 27px}
.pull-quote{color:var(--quote);font-weight:700;font-style:italic;font-size:10.6px;line-height:14.6px;margin:0 0 14.6px 33px;text-align:justify}
.features{list-style:none;margin:0 0 14.6px 0}
.features li{position:relative;padding-left:32px;text-align:justify;line-height:13.4px;margin-bottom:0}
.features li::before{content:"\2666";position:absolute;left:14px;top:0;font-size:9px}
.features--spaced{margin-top:14.6px}
.footer-num{position:absolute;left:0;right:0;top:660px;text-align:center;font-size:9px;color:var(--muted)}
.footer-title{position:absolute;left:0;right:0;top:676px;text-align:center;font-size:8.5px;color:var(--muted)}
</style>
</head>
<body>
<div class="ruler">·2·1·▫·1·2·3·4·5·6·7·8·9·10·11·12·13·14·15·16·17·18·19</div>

<section class="page page--left">
  <div class="page-brand">Statewide Learning Department</div>
  <div class="page-rule"></div>
  <div class="page-body">
    <p>how to guide their children through the college and career options facing them. Parents themselves may need the support of educators as well.</p>
    <h2 class="section-title">1.2&nbsp;History and Purpose of Early College High Schools</h2>
    <p class="indent">The Early College High School (BRVT) model began in 2002 with funding from the Harlan &amp; Mae Corbin Foundation to <em>improve college readiness and completion rates for students underrepresented in postsecondary education.</em></p>
    <p class="pull-quote">According to Paul Rendell, Executive Director of Education for the Corbin Foundation, “It’s no wonder students drop out: They are shuffled through the system with adults who hardly know them…. we need to engage and motivate students by giving them the personalized and rigorous courses they need to make a smooth transition to college or the workplace. Early college high school programs are an effective way to accomplish this.”</p>
    <p class="indent">This new model for high schools came about in response to the need to increase high-school graduation rates and equip <em>all</em> students with the skills they need to successfully complete college-level work and meet the needs of today’s workplace. Too many students are being left behind every day, unprepared to study further or secure good jobs in today’s economy. Now, however, we have a good change strategy—BRVTs, which respond to the needs of students who would otherwise be left behind, engaging and motivating them, and setting them on their way “early” to college.</p>
    <p class="indent">With the BRVT model, we raise the expectations traditionally underserved and high-risk students have for themselves by offering them access to advanced high-school courses and college courses. Students take a blend of high-school and college courses, simultaneously pursuing a high-school diploma <em>and</em> either an associate’s degree or up to two years’ college credits.</p>
    <p class="indent">The advantage of this approach is that students are exposed to higher education early in their lives.</p>
    <p style="margin-bottom:0">Several characteristics generally distinguish BRVTs. These include:</p>
    <ul class="features">
      <li>Their small size, typically with up to 100 students per grade level.</li>
      <li>Responsible growth. BRVTs typically begin in 9<sup style="font-size:7px">th</sup> grade and take four years to reach full capacity.</li>
      <li>A close proximity to the postsecondary partner, in some cases directly on the college campus.</li>
    </ul>
  </div>
  <div class="footer-num">- 7 -</div>
  <div class="footer-title">Policy Manual in Education</div>
</section>

<section class="page page--right">
  <div class="page-brand">Statewide Learning Department</div>
  <div class="page-rule"></div>
  <div class="page-body">
    <ul class="features">
      <li>Block scheduling of classes to allow for acceleration of the graduation requirements so students can simultaneously take college courses.</li>
      <li>Limited high school electives since most elective credits are earned through dual-credit coursework.</li>
    </ul>
    <p class="indent">Clearly, the BRVT model makes sense. It assumes students who engage in rigorous coursework in high school are better ready for college-level work and more likely to earn a postsecondary degree. And most impactful, the model remains true to its mission of engaging historically underrepresented student populations</p>
    <h2 class="section-title">1.3&nbsp; Comparisons of Early College High Schools with Other Dual Credit Programs</h2>
    <p class="indent">Over the past decades, other “accelerating” programs have been introduced to secondary school students. A short comparison of these with the BRVT model affirms the strength of BRVTs in making a difference in learning and achievement for so many students.</p>
    <p class="indent" style="margin-bottom:0">When comparing <strong>dual enrollment</strong> programs with BRVT, it becomes clear BRVTs are a more structured dual enrollment strategy specifically targeted at traditionally underserved students, and which has demonstrated its effectiveness in increasing postsecondary participation and attainment rates for this high-need population. Dual Enrollment differs from the BRVT model in very clear ways. A comparison of outcomes affirms this value of BRVTs versus dual enrollment:</p>
    <ul class="features features--spaced">
      <li>While dual-enrollment programs tend to draw students who are mid- to high-achieving, most students in BRVTs are minority (77%) and low-income (57%). Just 37% of dual enrollment students come from low-income families.</li>
      <li>In dual enrollment, students select individual courses that potentially allow them to earn both high-school and postsecondary credit. BRVTs present a cohesive curriculum <em>integrating</em> high-school and college-level coursework into a single program.</li>
    </ul>
    <p class="indent">A comparison of BRVTs with the Global Diploma (GD) programs show an even more marked difference from the dual enrollment and BRVT programs. While BRVT programs set a priority for enrollment on underserved and underrepresented student populations, GD programs do not target a specific population. In fact, research shows that both AT and GD programs offer the “biggest mismatch for students of color and students from economically disadvantaged backgrounds” due to the absence of appropriate and strong support services to help these often unprepared students to succeed<sup style="font-size:7px">2</sup></p>
  </div>
  <div class="footer-num">- 8 -</div>
  <div class="footer-title">Policy Manual in Education</div>
</section>

<div class="page page--next-left"></div>
<div class="page page--next-right"></div>
</body>
</html>
```